Homepage for Travel NFT Marketplace

Hi there!
We are building a Travel Marketplace that incorporates NFTs. We are looking for a full page redesign of the homepage for this marketplace.
You can find the instructions along with all the content here at https://www.filquarry.com/sh/7xq2mvplet9wd4k/BBKrtuMzqWenHoxKfPcVa3ghd?dl=0
We look forward to seeing your submissions!
Industry/Entity Type
Tourism
Number of Pages Required
1 page
Font styles to use
Sans Serif
Colors
0094D4
00A9DD
6FCCEA
C7EBF8
E9F6FB
00AB8E
00BBA5
67D7C9
C6EFE9
E9F9F6
F0912C
F2A743
F7CA91
FBE8D2
FDF5EE
A7469A
B969AE
D3A5CF
EDDBEB
F8F0F9
6B429C
8869AF
B7A5CE
E3DAEB
F3F0F8
Requirements
Must have
- Clean, Modern & Fun!
Should not have
- Messy or Overcrowded

```html
<!DOCTYPE html>
<html lang="en">
<head>
<meta charset="utf-8">
<title>Coin Roamers — Travel NFT Marketplace</title>
<link href="https://fonts.googleapis.com/css2?family=Lato:wght@400;700;900&family=Nunito+Sans:wght@400;600;700;800&display=swap" rel="stylesheet">
<style>
:root{
  --blue:#3fa9f5;
  --sky:#44aef0;
  --violet:#8a55dc;
  --magenta:#c81fbf;
  --ink:#1c1c24;
  --text:#3a3a44;
  --paper:#f1f2f5;
  --white:#ffffff;
  --accent:#c51bc0;
  --tile:#45aaf0;
}
*{margin:0;padding:0;box-sizing:border-box}
html,body{width:1200px;height:3661px;overflow:hidden}
body{position:relative;background:var(--paper);font-family:"Lato",sans-serif;color:var(--text)}
.abs{position:absolute}
.bg-shapes{position:absolute;left:0;top:0;width:1200px;height:3661px}

/* header */
.site-header{position:absolute;left:0;top:0;width:1200px;height:94px;background:var(--white);box-shadow:0 2px 8px rgba(0,0,0,.05)}
.brand{position:absolute;left:111px;top:28px;display:flex;align-items:center;gap:12px;font-family:"Nunito Sans",sans-serif;font-weight:600;font-size:21px;color:var(--ink)}
.brand-dot{width:34px;height:34px;border-radius:50%;background:var(--violet)}
.main-nav{position:absolute;left:408px;top:0;display:flex;height:94px}
.main-nav a{display:block;padding:0 18px;line-height:94px;font-size:15px;color:var(--ink);text-decoration:none}
.main-nav a.active{background:linear-gradient(#fff,#f0ecfa);border-bottom:3px solid var(--violet)}
.nav-tools{position:absolute;left:930px;top:28px;display:flex;gap:22px;align-items:center}
.round-btn{width:38px;height:38px;border-radius:50%;background:#e9e2f8;display:flex;align-items:center;justify-content:center}
.lang{color:var(--blue);font-weight:700;font-size:16px}

/* hero */
.hero-kicker{position:absolute;left:0;width:1200px;top:124px;text-align:center;font-family:"Nunito Sans",sans-serif;font-size:28px;font-weight:600;color:var(--ink);letter-spacing:.5px}
.hero-title{position:absolute;left:0;width:1200px;top:156px;text-align:center;font-family:"Nunito Sans",sans-serif;font-weight:800;font-size:37px;line-height:38px;background:linear-gradient(90deg,#a23ad9,#6b58e8 50%,#c21ec0);-webkit-background-clip:text;background-clip:text;color:transparent}
.hero-art{position:absolute;left:320px;top:225px;width:560px;height:420px;border-radius:40px;background:linear-gradient(160deg,#c8b8a8,#5a6fa8 60%,#3c4f86)}
.hero-balloons{position:absolute;left:20px;top:200px;width:1160px;height:160px;background:radial-gradient(circle at 10% 40%,#f4a4b0 0 22px,transparent 23px),radial-gradient(circle at 28% 60%,#b79ad6 0 26px,transparent 27px),radial-gradient(circle at 80% 60%,#f0a4a0 0 24px,transparent 25px),radial-gradient(circle at 92% 45%,#a9a3e0 0 18px,transparent 19px)}
.hero-word{position:absolute;left:0;width:1200px;top:505px;text-align:center;font-family:"Nunito Sans",sans-serif;font-weight:800;font-size:118px;line-height:120px;letter-spacing:2px;background:linear-gradient(90deg,#20b8f0,#8a55dc 55%,#c81fbf);-webkit-background-clip:text;background-clip:text;color:transparent}

/* welcome */
.welcome{position:absolute;left:0;width:1200px;top:835px;text-align:center}
.welcome h2{font-family:"Nunito Sans",sans-serif;font-size:31px;font-weight:800;color:var(--ink)}
.welcome h2 span{background:linear-gradient(90deg,#3fa9f5,#a043d8);-webkit-background-clip:text;background-clip:text;color:transparent}
.welcome p{margin:14px auto 0;width:670px;font-size:15px;line-height:24px;color:var(--ink)}
.btn{display:inline-flex;align-items:center;gap:8px;margin-top:18px;height:42px;padding:0 20px;background:var(--accent);color:#fff;font-weight:900;font-size:14px;text-decoration:none}

/* apart */
.apart-title{position:absolute;left:0;width:1200px;top:1302px;text-align:center;font-family:"Nunito Sans",sans-serif;font-weight:800;font-size:31px;color:#fff}
.spine{position:absolute;left:594px;top:1378px;width:8px;height:545px;background:#fff}
.step{position:absolute}
.step .num{position:absolute;font-family:"Nunito Sans",sans-serif;font-weight:800;font-size:18px;color:var(--accent);opacity:.8}
.step.right .num{color:#6cd7f7;opacity:.6}
.step h3{position:absolute;font-family:"Nunito Sans",sans-serif;font-weight:700;font-size:21px;color:#fff;white-space:nowrap}
.step p{position:absolute;width:270px;font-size:13px;line-height:19px;color:#fff}
.step.left p{text-align:right}
.step.right p{text-align:justify}
.step .pic{position:absolute;border-radius:16px;opacity:.9}
.hex-end{position:absolute;left:528px;top:1915px;width:140px;height:140px;border-radius:50%;background:#fff}

/* nft */
.nft-title{position:absolute;left:0;width:1200px;top:2300px;text-align:center;font-family:"Nunito Sans",sans-serif;font-weight:800;font-size:31px;color:var(--ink)}
.nft-title span{color:var(--blue)}
.nft-grid{position:absolute;left:111px;top:2386px;display:grid;grid-template-columns:repeat(4,230px);gap:15px 19px}
.nft-card{height:212px;background:linear-gradient(180deg,#45aaf0,#3da3ec)}

/* stats */
.stats{position:absolute;left:0;top:3098px;width:1200px;display:flex;justify-content:space-around;padding:0 110px;color:#fff;text-align:center}
.stat{width:300px;display:flex;flex-direction:column;align-items:center}
.stat-icon{width:78px;height:78px;border-radius:50%;background:#fff;display:flex;align-items:center;justify-content:center}
.stat b{margin-top:16px;font-size:20px;font-weight:700}
.stat span{margin-top:4px;font-size:17px;font-weight:700}

/* footer */
.rule{position:absolute;left:0;width:1200px;height:1px;background:rgba(255,255,255,.45)}
.foot-brand{position:absolute;left:111px;top:3304px;display:flex;align-items:center;gap:16px;font-family:"Nunito Sans",sans-serif;font-size:28px;color:#fff}
.foot-brand i{display:block;width:64px;height:64px;border-radius:50%;background:#fff;opacity:.9}
.foot-about{position:absolute;left:111px;top:3394px;width:310px;font-size:15px;line-height:26px;color:#fff}
.foot-col{position:absolute;top:3296px;color:#fff}
.foot-col h4{font-family:"Nunito Sans",sans-serif;font-weight:800;font-size:19px;margin-bottom:8px}
.foot-col a{display:block;color:#fff;text-decoration:none;font-size:15px;line-height:25px;padding-left:2px}
.foot-col.biz a{line-height:32px}
.social a{display:flex;align-items:center;gap:12px;line-height:45px}
.social i{display:block;width:30px;height:30px;border:2px solid #fff;border-radius:50%}
.copy{position:absolute;left:0;width:1200px;top:3589px;text-align:center;color:#fff;font-size:15px}
</style>
</head>
<body>

<svg class="bg-shapes" viewBox="0 0 1200 3661" aria-hidden="true">
  <defs>
    <linearGradient id="mist" x1="0" y1="0" x2="0" y2="1">
      <stop offset="0" stop-color="#f6f7fa"/><stop offset=".5" stop-color="#dfe3ec"/><stop offset="1" stop-color="#eceef2"/>
    </linearGradient>
    <linearGradient id="band" x1="0" y1="0" x2="1" y2=".35">
      <stop offset="0" stop-color="#3fb0f5"/><stop offset=".5" stop-color="#8a55dc"/><stop offset="1" stop-color="#c81fbf"/>
    </linearGradient>
    <linearGradient id="stripeL" x1="0" y1="0" x2="1" y2="0">
      <stop offset="0" stop-color="#5a5ef0"/><stop offset="1" stop-color="#a43be0"/>
    </linearGradient>
    <linearGradient id="stripeR" x1="0" y1="0" x2="1" y2="0">
      <stop offset="0" stop-color="#b02ad8"/><stop offset="1" stop-color="#d21fc0"/>
    </linearGradient>
  </defs>
  <rect x="0" y="94" width="1200" height="1050" fill="url(#mist)"/>
  <path d="M0 300 L180 260 L360 330 L520 280 L700 320 L900 250 L1200 290 L1200 640 Q900 800 600 770 Q300 740 0 620 Z" fill="#cdd2dc" opacity=".6"/>
  <polygon points="100,585 500,690 470,712 100,600" fill="url(#stripeL)"/>
  <polygon points="1200,640 1200,660 1040,770 1000,752" fill="url(#stripeR)"/>
  <path d="M0 1210 L420 1125 L1200 1215 L1200 2085 L880 2250 L600 2120 L320 2040 L0 2100 Z" fill="url(#band)"/>
  <path d="M0 2250 Q300 2240 600 2300 L1200 2320 L1200 2880 L0 2880 Z" fill="#eceef2"/>
  <path d="M0 3065 Q150 2950 260 2925 Q360 2905 420 2950 L1200 2930 L1200 3661 L0 3661 Z" fill="url(#band)"/>
</svg>

<header class="site-header">
  <div class="brand"><span class="brand-dot"></span>Coin Roamers</div>
  <nav class="main-nav">
    <a class="active" href="#">Home</a><a href="#">About Us</a><a href="#">NFT</a><a href="#">Trips</a><a href="#">Auctions</a><a href="#">The POt</a>
  </nav>
  <div class="nav-tools">
    <span class="round-btn"><svg width="16" height="16" viewBox="0 0 16 16"><circle cx="8" cy="6" r="3" fill="none" stroke="#8a55dc" stroke-width="1.6"/><path d="M2 15c1-4 11-4 12 0" fill="none" stroke="#8a55dc" stroke-width="1.6"/></svg></span>
    <span class="round-btn"><svg width="18" height="18" viewBox="0 0 18 18"><circle cx="9" cy="9" r="7" fill="none" stroke="#8a55dc" stroke-width="1.5"/><path d="M2 9h14M9 2c3 3 3 11 0 14M9 2c-3 3-3 11 0 14" fill="none" stroke="#8a55dc" stroke-width="1.2"/></svg></span>
    <span class="lang">⌄ Eng</span>
  </div>
</header>

<section class="hero">
  <div class="hero-balloons" role="img" aria-label="Hot air balloons and map pins floating in the sky"></div>
  <div class="hero-kicker">BRIDGING THE GAP BETWEEN</div>
  <div class="hero-title">CRYPTO &amp;AMP Real World<br>ADVENTURES</div>
  <div class="hero-art" role="img" aria-label="Illustration of a group of backpackers celebrating together"></div>
  <div class="hero-word">NOMADS</div>
</section>

<section class="welcome">
  <h2>WELCOME TO <span>COIN ROAMERS</span></h2>
  <p>The World’s First Blockchain Travel Marketplace . Our adventures are available exclusively to those holding a certain NFT in their wallet</p>
  <a class="btn" href="#">READ MORE <svg width="14" height="14" viewBox="0 0 14 14"><circle cx="7" cy="7" r="6.5" fill="#fff"/><path d="M5.5 4l3 3-3 3" stroke="#c51bc0" stroke-width="1.8" fill="none"/></svg></a>
</section>

<section class="apart">
  <h2 class="apart-title">WHAT SETS US APART?</h2>
  <div class="spine"></div>
  <svg class="abs" style="left:470px;top:1415px" width="260" height="460" viewBox="0 0 260 460" aria-hidden="true">
    <g fill="#fff">
      <polygon points="130,8 228,8 255,17 228,26 130,26"/>
      <polygon points="128,92 30,92 3,101 30,110 128,110"/>
      <polygon points="130,180 228,180 255,189 228,198 130,198"/>
      <polygon points="128,264 30,264 3,273 30,282 128,282"/>
      <polygon points="130,350 228,350 255,359 228,368 130,368"/>
      <polygon points="128,436 30,436 3,445 30,454 128,454"/>
    </g>
  </svg>

  <div class="step right"><span class="num" style="left:613px;top:1397px">STEP 01</span>
    <div class="pic" role="img" aria-label="Two hikers with backpacks" style="left:905px;top:1340px;width:120px;height:105px;background:linear-gradient(#d9b36b,#5e6f9f)"></div>
    <h3 style="left:747px;top:1418px">The Adventures!</h3>
    <p style="left:752px;top:1451px">We dig deep in our research &amp;amp; work with local guides to create unique experiences not found anywhere else.</p></div>

  <div class="step left"><span class="num" style="left:504px;top:1480px">STEP 02</span>
    <div class="pic" role="img" aria-label="Off-road vehicle loaded with luggage" style="left:145px;top:1438px;width:120px;height:95px;background:linear-gradient(#9bb54a,#5d6b2d)"></div>
    <h3 style="left:275px;top:1502px">Intentional Travel</h3>
    <p style="left:178px;top:1535px">We give you the ability to have a meaningful impact on local communities and offset the emissions from your</p></div>

  <div class="step right"><span class="num" style="left:613px;top:1570px">STEP 03</span>
    <div class="pic" role="img" aria-label="Travellers walking with gear" style="left:918px;top:1522px;width:125px;height:100px;background:linear-gradient(#a98a58,#4b5a3a)"></div>
    <h3 style="left:757px;top:1592px">Keep it Simple</h3>
    <p style="left:752px;top:1624px">No planning, no stress... Just arrive at your destination and our guides will take it from there!</p></div>

  <div class="step left"><span class="num" style="left:504px;top:1653px">STEP 04</span>
    <div class="pic" role="img" aria-label="Picnic spot under trees" style="left:160px;top:1612px;width:95px;height:92px;background:linear-gradient(#7cb24a,#c58fb8)"></div>
    <h3 style="left:285px;top:1675px">Fellow Nomads</h3>
    <p style="left:178px;top:1708px">For group trips, you will meet like-minded folk within the Coin Roamers communityon your adventures.</p></div>

  <div class="step right"><span class="num" style="left:613px;top:1748px">STEP 05</span>
    <div class="pic" role="img" aria-label="Travellers greeting each other with luggage" style="left:965px;top:1688px;width:150px;height:118px;background:linear-gradient(#e48b7b,#4f4f8c)"></div>
    <h3 style="left:748px;top:1770px">Customer Experience</h3>
    <p style="left:752px;top:1803px">After booking a trip, all correspondence is done through Parley, which is quick, easy and efficient.</p></div>

  <div class="step left"><span class="num" style="left:504px;top:1832px">STEP 06</span>
    <div class="pic" role="img" aria-label="Person holding cryptocurrency coin and card" style="left:185px;top:1780px;width:100px;height:105px;background:linear-gradient(#e08a7a,#4a66b8)"></div>
    <h3 style="left:272px;top:1854px">Pure Crypto Baby!</h3>
    <p style="left:178px;top:1887px">The world’s first travel agency to exclusively accept cryptocurrencies. That’s right, we&amp;#39;re a crypto only</p></div>

  <div class="hex-end"></div>
</section>

<section class="nft">
  <h2 class="nft-title">COIN ROAMERS <span>NFT</span></h2>
  <div class="nft-grid">
    <div class="nft-card" role="img" aria-label="NFT character artwork: bearded figure in hat and sunglasses"></div>
    <div class="nft-card" role="img" aria-label="NFT character artwork: ape with cap and visor glasses"></div>
    <div class="nft-card" role="img" aria-label="NFT character artwork: long-eared creature with mask"></div>
    <div class="nft-card" role="img" aria-label="NFT character artwork: ape in cap and suspenders"></div>
    <div class="nft-card" role="img" aria-label="NFT character artwork: penguin with scarf and sunglasses"></div>
    <div class="nft-card" role="img" aria-label="NFT character artwork: bear with toothy grin"></div>
    <div class="nft-card" role="img" aria-label="NFT character artwork: creature in beanie and chain"></div>
    <div class="nft-card" role="img" aria-label="NFT character artwork: penguin in knit hat"></div>
  </div>
</section>

<section class="stats">
  <div class="stat"><span class="stat-icon"><svg width="36" height="40" viewBox="0 0 36 40"><path d="M18 2l15 6v11c0 10-7 16-15 19C10 35 3 29 3 19V8z" fill="none" stroke="#8a55dc" stroke-width="3"/><path d="M11 20l5 5 9-10" fill="none" stroke="#3fa9f5" stroke-width="3"/></svg></span><b>$1,120,546</b><span>Donated To Charity</span></div>
  <div class="stat"><span class="stat-icon"><svg width="40" height="40" viewBox="0 0 40 40"><circle cx="20" cy="20" r="5" fill="#8a55dc"/><path d="M6 6l9 9M34 6l-9 9M6 34l9-9M34 34l-9-9M20 2v8M20 30v8" stroke="#3fa9f5" stroke-width="3"/></svg></span><b>$456,060</b><span>Given In prizes to Our Community</span></div>
  <div class="stat"><span class="stat-icon"><svg width="36" height="40" viewBox="0 0 36 40"><circle cx="16" cy="6" r="4" fill="#3fa9f5"/><path d="M14 12l-4 12 8 4-2 10M14 12l8 8 6-2M10 24l-6 10" fill="none" stroke="#8a55dc" stroke-width="3"/></svg></span><b>$56,060</b><span>In the Adventure Pot</span></div>
</section>

<footer>
  <div class="rule" style="top:3266px"></div>
  <div class="foot-brand"><i></i>Coin Roamers</div>
  <p class="foot-about">Lorem ipsum dolor sit amet, consectetur adipiscing elit, sed do eiusmod tempor incididunt ut labore et dolore magna</p>
  <div class="foot-col" style="left:520px"><h4>USE LINK</h4><a href="#">Home</a><a href="#">About Us</a><a href="#">NFT</a><a href="#">Trips</a><a href="#">Auctions</a><a href="#">The POt</a></div>
  <div class="foot-col biz" style="left:720px"><h4>BUSINESS</h4><a href="#">Terms&amp;condtions</a><a href="#">Privacy Policy</a><a href="#">Support</a><a href="#">Testimonials</a></div>
  <div class="foot-col social" style="left:946px"><h4>FOLLOW US</h4><a href="#"><i></i>Friendbook</a><a href="#"><i></i>Linkwork</a><a href="#"><i></i>Snapgram</a><a href="#"><i></i>Chirper</a></div>
  <div class="rule" style="top:3550px"></div>
  <p class="copy">Copyrights © 2022 Coin Roamers. All Rights Reserved.</p>
</footer>

</body>
</html>
```